Geschäftspapiere für Unternehmensberatung
Zielgruppe
Unternehmensberatung
Aufgabenstellung
Es soll eine Word-Vorlage als Geschäftsbrief sein.
Name, Adresse, Steuernummer, Bank können als Platzhalter angegeben werden
WICHTIG: es soll auch selbst geduckt werden können, ohne das das Logo verpixelt oder ähnliches

```html
<!DOCTYPE html>
<html lang="de">
<head>
<meta charset="utf-8">
<title>VERANTA GmbH – Geschäftsbrief</title>
<link rel="stylesheet" href="https://fonts.googleapis.com/css2?family=Arimo:wght@400&family=Open+Sans:wght@400;700&display=swap">
<style>
  :root{
    --bg:#e9e9e9;
    --paper:#ffffff;
    --brand:#8dc63f;
    --slate:#4d4f5c;
    --ink:#3a3a3a;
    --muted:#555;
    --faint:#f1f1f1;
    --sign:#1f2d8a;
  }
  *{box-sizing:border-box;margin:0;padding:0}
  html,body{width:1200px;height:1010px;overflow:hidden;background:var(--bg)}
  .letter{
    position:absolute;left:267px;top:35px;width:666px;height:940px;
    background:var(--paper);box-shadow:0 6px 22px rgba(0,0,0,.12);
    font-family:"Arimo",Arial,sans-serif;color:var(--ink);overflow:hidden;
  }
  .brand{position:absolute;right:60px;top:40px;display:flex;align-items:center;gap:8px}
  .brand__mark{width:14px;height:14px;background:var(--slate)}
  .brand__name{font-family:"Open Sans",sans-serif;font-weight:700;font-size:34px;letter-spacing:1px;color:var(--brand)}
  .brand-rule{position:absolute;right:60px;top:92px;width:210px;border-top:1px solid var(--slate)}
  .sender{
    position:absolute;left:420px;top:112px;padding-left:12px;border-left:1px solid var(--slate);
    font-family:"Open Sans",sans-serif;font-size:8.5px;line-height:1.45;color:var(--ink);font-style:normal
  }
  .sender__contact{list-style:none;margin-top:4px;padding-left:14px}
  .sender__contact li{display:flex;align-items:center;gap:5px}
  .sender__contact svg{width:8px;height:8px;fill:var(--brand);flex:none}
  .return-line{
    position:absolute;left:70px;top:200px;font-family:"Open Sans",sans-serif;font-size:7px;
    text-decoration:underline;color:var(--ink)
  }
  .return-line span{color:var(--brand)}
  .fold{position:absolute;left:0;width:16px;border-top:1px solid #bbb}
  .watermark{
    position:absolute;right:40px;top:655px;font-family:"Open Sans",sans-serif;font-weight:700;
    font-size:80px;line-height:1;color:var(--faint);letter-spacing:3px;white-space:nowrap
  }
  .body{position:absolute;left:95px;top:310px;width:480px;font-size:11.5px;line-height:1.42}
  .body p{margin-bottom:14px}
  .closing{margin-top:20px}
  .signature{width:130px;height:42px;margin:12px 0 4px;background:linear-gradient(90deg,#eef0fa,#f7f8fd);border-radius:4px}
  .footer{
    position:absolute;left:70px;right:50px;bottom:40px;display:flex;align-items:flex-end;
    font-family:"Open Sans",sans-serif;font-size:8.5px;line-height:1.45;color:var(--ink)
  }
  .footer__col{flex:1;white-space:nowrap}
  .footer__sep{width:1px;height:22px;background:var(--slate);margin:0 18px}
</style>
</head>
<body>
<main class="letter">
  <header>
    <div class="brand"><span class="brand__mark"></span><span class="brand__name">VERANTA</span></div>
    <div class="brand-rule"></div>
    <address class="sender">
      VERANTA GmbH<br>Muster Weg 32<br>10400 Muster Stadt
      <ul class="sender__contact">
        <li><svg viewBox="0 0 10 10"><circle cx="5" cy="5" r="5"/></svg>+49 (0) 123 000 456 00</li>
        <li><svg viewBox="0 0 10 10"><rect width="10" height="10" rx="2"/></svg>+49 (0) 123 000 456 99</li>
        <li><svg viewBox="0 0 10 10"><rect y="2" width="10" height="7"/></svg>info@veranta.de</li>
        <li><svg viewBox="0 0 10 10"><circle cx="5" cy="5" r="5"/></svg>www.veranta.de</li>
      </ul>
    </address>
  </header>

  <div class="return-line">VERANTA GmbH <span>|</span> Muster Weg 32 <span>|</span> 10400 Muster Stadt</div>

  <div class="fold" style="top:332px"></div>
  <div class="fold" style="top:470px"></div>
  <div class="fold" style="top:628px"></div>

  <div class="watermark" aria-hidden="true">VERANTA</div>

  <section class="body">
    <p>Sehr geehrte Damen und Herren,</p>
    <p>In sollicitudin, metus et posuere blandit, erat dui bibendum eros, id vestibulum sem justo vel mauris. Ut tempor dolor ut justo vulputate, eu blandit libero faucibus. In laoreet, massa non ultricies tempor, est enim auctor mi, sit amet venenatis massa augue in justo. Praesent eu tincidunt diam. Maecenas id mi efficitur tellus interdum consectetur vel sed ante. Sed suscipit quis eros a fermentum. Curabitur ornare sit amet leo eu semper. Vestibulum pretium mi eu nisi. gadde.</p>
    <p>Sed nunc est, iaculis vel enim ut, fringilla commodo lorem. Pellentesque facilisis tempus lorem eget porttitor. Morbi accumsan, nulla accumsan mollis maximus, lectus diam venenatis odio, quis bibendum elit ex a arcu. Fusce turpis erat, euismod sit amet dolor eu, hendrerit rhoncus libero. Phasellus convallis, mi vel pharetra sollicitudin, nisi purus maximus est, nec lobortis dolor enim et augue. Vestibulum auctor mi sit amet leo auctor egestas. Pellentesque eget endrerit rhoncus dan.</p>
    <p class="closing">Mit freundlichen Grüßen</p>
    <div class="signature" role="img" aria-label="Handschriftliche Unterschrift von Hans Muster"></div>
    <p>Hans Muster, LL.M.</p>
  </section>

  <footer class="footer">
    <div class="footer__col">Bankverbindung:<br>Sparkasse Nordtal</div>
    <div class="footer__sep"></div>
    <div class="footer__col">BIC: NRDTDE11XXX<br>IBAN: DE00 1234 5678 9012 3456 00</div>
    <div class="footer__sep"></div>
    <div class="footer__col">Steuernummer: 000/000/00000<br>Umsatzsteuer-ID-Nr.: DE 000000000</div>
  </footer>
</main>
</body>
</html>
```